Business Cards

I'd like help creating business cards with the full logo "Veltrona Capital Partners" on the back of the card (navy background with white writing), and abbreviated logo "VCP" on the front. Would like to list name, title, phone number, email, and website listed on front of card. Would like to keep very simple. Front font Arial or similar.

```html
<!DOCTYPE html>
<html lang="en">
<head>
<meta charset="UTF-8">
<title>Veltrona Capital Partners – Business Cards</title>
<link rel="stylesheet" href="https://fonts.googleapis.com/css2?family=Montserrat:wght@400;500;600;700&display=swap">
<style>
  :root {
    --backdrop: #1e1e1f;
    --navy: #213a6c;
    --navy-deep: #1b3161;
    --paper: #ffffff;
    --ink-soft: #2e4477;
  }
  * { box-sizing: border-box; margin: 0; padding: 0; }
  html, body {
    width: 1200px; height: 939px; overflow: hidden;
    background: var(--backdrop);
    font-family: "Montserrat", Arial, sans-serif;
  }
  .canvas { position: relative; width: 1200px; height: 939px; }

  .card {
    position: absolute;
    width: 600px; height: 340px;
    border-radius: 2px;
    overflow: hidden;
  }

  /* Back of card */
  .card-back {
    left: 150px; top: 110px;
    background: var(--navy);
    display: flex; align-items: center; justify-content: center;
  }
  .brand-full {
    color: var(--paper);
    font-weight: 600;
    text-align: center;
    text-transform: uppercase;
    line-height: 1.15;
  }
  .brand-full .word-main { display: block; font-size: 52px; letter-spacing: 2px; }
  .brand-full .word-sub { display: block; font-size: 21px; letter-spacing: 7px; }

  /* Front of card */
  .card-front {
    left: 460px; top: 490px;
    background: var(--paper);
    color: var(--navy);
  }
  .brand-short {
    position: absolute; right: 48px; top: 36px;
    font-size: 54px; font-weight: 600; letter-spacing: 1px; line-height: 1;
    color: var(--navy);
  }
  .person-name {
    position: absolute; left: 40px; top: 152px;
    font-size: 22px; font-weight: 700; letter-spacing: 1px; line-height: 1;
    color: var(--navy);
  }
  .divider-long {
    position: absolute; left: 40px; right: 30px; top: 182px;
    height: 1.5px; background: var(--navy);
  }
  .person-title {
    position: absolute; left: 40px; top: 190px;
    font-size: 14px; font-weight: 400; line-height: 1.2; color: var(--ink-soft);
  }
  .office {
    position: absolute; right: 30px; top: 190px;
    font-style: normal;
    text-align: right; font-size: 13px; line-height: 1.45; color: var(--ink-soft);
  }
  .office-name { font-weight: 700; color: var(--navy); }
  .divider-short {
    position: absolute; left: 40px; top: 224px;
    width: 170px; height: 1.5px; background: var(--navy);
  }
  .contact-list {
    position: absolute; left: 40px; top: 234px;
    list-style: none; font-size: 13px; line-height: 20px; color: var(--ink-soft);
  }
  .contact-list li { display: flex; align-items: center; gap: 8px; }
  .contact-list svg { width: 11px; height: 11px; fill: var(--navy); flex: none; }
  .band {
    position: absolute; bottom: 0; height: 20px; background: var(--navy-deep);
  }
  .band-left { left: 0; width: 72%; }
  .band-right { right: 0; width: calc(28% - 8px); }
</style>
</head>
<body>
<main class="canvas">

  <section class="card card-back" aria-label="Card back">
    <h1 class="brand-full">
      <span class="word-main">Veltrona</span>
      <span class="word-sub">Capital Partners</span>
    </h1>
  </section>

  <section class="card card-front" aria-label="Card front">
    <div class="brand-short">VCP</div>

    <div class="person-name">DANIEL REYES</div>
    <div class="divider-long"></div>
    <div class="person-title">Managing Director</div>

    <address class="office">
      <div class="office-name">Veltrona Capital Partners</div>
      <div>4728 Harlow Drive, Ste 03</div>
      <div>Brookfield, CT 06804</div>
    </address>

    <div class="divider-short"></div>

    <ul class="contact-list">
      <li>
        <svg viewBox="0 0 24 24" aria-hidden="true"><path d="M6.6 10.8a15.1 15.1 0 0 0 6.6 6.6l2.2-2.2a1 1 0 0 1 1-.25 11.4 11.4 0 0 0 3.6.57 1 1 0 0 1 1 1V20a1 1 0 0 1-1 1A17 17 0 0 1 3 4a1 1 0 0 1 1-1h3.5a1 1 0 0 1 1 1c0 1.25.2 2.45.57 3.57a1 1 0 0 1-.25 1z"/></svg>
        (323) 555-0148
      </li>
      <li>
        <svg viewBox="0 0 24 24" aria-hidden="true"><path d="M2 5h20v2l-10 7L2 7z M2 9.5l10 7 10-7V19H2z"/></svg>
        info@veltronacapitalpartners.com
      </li>
      <li>
        <svg viewBox="0 0 24 24" aria-hidden="true"><circle cx="12" cy="12" r="10"/></svg>
        VeltronaCapitalPartners.com
      </li>
    </ul>

    <div class="band band-left"></div>
    <div class="band band-right"></div>
  </section>

</main>
</body>
</html>
```